Wordpress Design Project

We are a Computer / Information Technology Company that will focus on the after-hours technical support for Home and Businesses.

I'm looking to have the home page as a static page with a links to blog, about us.

www.qmvolt.com.au is my web site.

Please do not chage uploaded logo's, do not copy current logo on website use uploaded files only, thanks.
Updates

Cheers

Derek

Target Market(s)

Home and Small office/home office, or SOHO Computer users.

Industry/Entity Type

Computer

Requirements
Should not have
• After hours tech support added to logo.

```html
<!DOCTYPE html>
<html lang="en">
<head>
<meta charset="utf-8">
<title>QM Volt – After Hours Technical Support</title>
<link href="https://fonts.googleapis.com/css2?family=Source+Sans+3:ital,wght@0,400;0,600;1,400;1,600&family=Arimo:ital,wght@0,400;1,700&display=swap" rel="stylesheet">
<style>
  :root {
    --blue-dark: #0158a6;
    --blue-mid: #0a78c0;
    --blue-light: #05a0e4;
    --brand-blue: #1f74c4;
    --heading-blue: #1563ad;
    --grey-light: #f3f3f3;
    --grey-mid: #c9cacd;
    --grey-deep: #a9abae;
    --ink: #111111;
    --white: #ffffff;
  }
  * { box-sizing: border-box; margin: 0; padding: 0; }
  html, body { width: 1173px; height: 1200px; overflow: hidden; }
  body {
    position: relative;
    background: var(--grey-light);
    font-family: "Source Sans 3", sans-serif;
    color: var(--ink);
  }

  /* Header */
  .site-header {
    position: absolute; left: 0; top: 0; width: 1173px; height: 84px;
    background: linear-gradient(#f4f4f4 0%, #d4d5d7 45%, #f6f6f6 100%);
  }
  .brand {
    position: absolute; display: flex; align-items: center; gap: 10px;
    font-family: "Source Sans 3", sans-serif; font-weight: 600;
    font-size: 34px; color: var(--brand-blue); letter-spacing: 0.5px;
  }
  .brand-dot { width: 30px; height: 30px; border-radius: 50%; background: var(--brand-blue); }
  .site-header .brand { left: 268px; top: 16px; }
  .main-nav { position: absolute; left: 659px; top: 29px; display: flex; gap: 10px; }
  .main-nav a {
    display: block; width: 75px; height: 27px; line-height: 27px; text-align: center;
    border-radius: 4px; font-size: 12px; text-decoration: none; color: var(--blue-dark);
    background: linear-gradient(#ffffff, #e6e7e8);
    box-shadow: 0 1px 2px rgba(0,0,0,.15);
  }
  .main-nav a.is-current {
    color: var(--white);
    background: linear-gradient(#1a8ee0, #0060b0);
  }

  /* Hero band */
  .hero-band {
    position: absolute; left: 0; top: 84px; width: 1173px; height: 453px;
    background:
      linear-gradient(var(--blue-dark), var(--blue-mid) 227px, #0a6fb8 227px, var(--blue-light) 100%);
  }
  .slider {
    position: absolute; left: 197px; top: 27px; width: 786px; height: 382px;
    border-radius: 7px; overflow: hidden;
    box-shadow: 0 3px 10px rgba(0,0,0,.35);
  }
  .slide-photo {
    position: absolute; inset: 0;
    background:
      linear-gradient(90deg, #2a2a2c 0%, #303032 38%, #eeeeef 41%, #f6f6f6 100%);
  }
  .slide-caption {
    position: absolute; right: 18px; bottom: 14px;
    font-family: "Source Sans 3", sans-serif; font-weight: 600;
    font-size: 29px; color: var(--brand-blue); letter-spacing: -0.2px;
  }
  .slider-dots { position: absolute; left: 551px; top: 425px; display: flex; gap: 7px; }
  .slider-dots span {
    width: 12px; height: 12px; border-radius: 50%;
    background: radial-gradient(circle at 40% 35%, #ffffff, #c8c8c8);
  }
  .slider-dots span.is-active { background: radial-gradient(circle at 40% 35%, #ffe98a, #f0b400); }

  /* Content */
  .content-area {
    position: absolute; left: 0; top: 537px; width: 1173px; height: 578px;
    background: linear-gradient(#c6c7ca 0%, #e4e4e5 45%, #f5f5f5 100%);
  }
  .page-main { position: absolute; left: 193px; top: 25px; width: 489px; }
  .page-title {
    font-family: "Arimo", sans-serif; font-style: italic; font-weight: 700;
    font-size: 29px; line-height: 1; margin-bottom: 22px;
  }
  .page-main p {
    font-family: "Arimo", sans-serif; font-size: 16.2px; line-height: 20.1px;
    text-align: justify; margin-bottom: 20px;
  }

  .sidebar {
    position: absolute; left: 696px; top: 30px; width: 292px; height: 523px;
    background: linear-gradient(#c8c9cc, #f3f3f3 70%);
    border: 1px solid #b9babc; box-shadow: 0 2px 4px rgba(0,0,0,.25);
  }
  .sidebar::after {
    content: ""; position: absolute; left: 4px; right: 4px; bottom: 0; height: 18px;
    background: #fafafa; border-radius: 20px 20px 0 0;
  }
  .search-box {
    position: absolute; left: 10px; top: 16px; width: 272px; height: 36px;
    border-radius: 18px; background: linear-gradient(#ffffff, #e4e4e4);
    box-shadow: inset 0 1px 3px rgba(0,0,0,.3);
  }
  .search-button {
    position: absolute; right: 0; top: 0; width: 82px; height: 36px; border-radius: 12px 18px 18px 12px;
    background: linear-gradient(#2aa3ee, #0066c0); color: var(--white);
    font-style: italic; font-size: 21px; line-height: 36px; text-align: center;
  }
  .widget { position: absolute; left: 26px; }
  .widget h2 {
    font-style: italic; font-weight: 600; font-size: 22.5px; line-height: 24px; color: var(--heading-blue);
  }
  .widget li {
    list-style: none; font-style: italic; font-size: 16.5px; line-height: 20.5px; color: var(--ink);
  }

  /* Footer */
  .site-footer {
    position: absolute; left: 0; top: 1115px; width: 1173px; height: 85px;
    background: linear-gradient(var(--blue-dark), var(--blue-mid) 50%, #0a6fb8 50%, var(--blue-light));
  }
  .footer-brand-panel {
    position: absolute; left: 260px; top: -16px; width: 243px; height: 101px;
    border-radius: 10px 10px 0 0; background: linear-gradient(#f1f1f1, #c7c8ca);
  }
  .footer-brand-panel .brand { left: 8px; top: 30px; }
  .footer-nav { position: absolute; left: 666px; top: 17px; display: flex; gap: 20px; }
  .footer-nav a { color: var(--white); text-decoration: none; font-size: 19px; }
  .copyright {
    position: absolute; left: 680px; top: 50px; color: var(--white); font-size: 14px;
  }
</style>
</head>
<body>
  <header class="site-header">
    <div class="brand"><span class="brand-dot"></span>QM Volt</div>
    <nav class="main-nav">
      <a class="is-current" href="#">HOME</a>
      <a href="#">ABOUT US</a>
      <a href="#">BLOG</a>
    </nav>
  </header>

  <section class="hero-band">
    <div class="slider">
      <div class="slide-photo" role="img" aria-label="Businessman in a dark suit offering a handshake beside a black desktop tower and monitor"></div>
      <p class="slide-caption">AFTER HOURS TECHNICAL SUPPORT</p>
    </div>
    <div class="slider-dots"><span class="is-active"></span><span></span><span></span><span></span></div>
  </section>

  <section class="content-area">
    <main class="page-main">
      <h1 class="page-title">HOME</h1>
      <p>Lorem ipsum dolor sit amet, consectetuer adipiscing elit. Nam cursus. Morbi ut mi. Nullam enim leo, egestas id, condimentum at, laoreet mattis, massa. Sed eleifend nonummy diam. Praesent mauris ante, elementum et, bibendum at, posuere sit amet, nibh. Duis tincidunt lectus quis dui viverra vestibulum. Suspendisse vulputate aliquam dui. Nulla elementum dui ut augue. Aliquam vehicula mi at mauris. Maecenas placerat, nisl at consequat rhoncus, sem nunc gravida justo, quis eleifend arcu velit quis lacus. Morbi magna magna, tincidunt a, mattis non, imperdiet vitae, tellus. Sed odio est, auctor ac, sollicitudin in, consequat vitae, orci. Fusce id felis. Vivamus sollicitudin metus eget eros.</p>
      <p>Pellentesque habitant morbi tristique senectus et netus et malesuada fames ac turpis egestas. In posuere felis nec tortor. Pellentesque faucibus. Ut accumsan ultricies elit. Maecenas at justo id velit placerat molestie. Donec dictum lectus non odio. Cras a ante vitae enim iaculis aliquam. Mauris nunc quam, venenatis nec, euismod sit amet, egestas placerat, est. Pellentesque habitant morbi tristique senectus et netus et malesuada fames ac turpis egestas. Cras id elit. Integer quis urna. Ut ante enim, dapibus malesuada, fringilla eu, condimentum quis, tellus. Aenean porttitor eros vel dolor. Donec convallis pede venenatis nibh. Duis quam. Nam eget lacus. Aliquam erat volutpat. Quisque dignissim congue leo.</p>
    </main>

    <aside class="sidebar">
      <div class="search-box"><span class="search-button">Search</span></div>
      <div class="widget" style="top:77px"><h2>Recent Posts</h2><ul><li>Fenestra XP sysprep</li></ul></div>
      <div class="widget" style="top:148px"><h2>Recent Comments</h2></div>
      <div class="widget" style="top:198px"><h2>Archives</h2><ul><li>September 2011</li></ul></div>
      <div class="widget" style="top:271px"><h2>Categories</h2><ul><li>Fenestra</li></ul></div>
      <div class="widget" style="top:343px"><h2>Meta</h2><ul><li>Log in</li><li>Entries RSS</li><li>Comments RSS</li><li>PressKit.org</li></ul></div>
    </aside>
  </section>

  <footer class="site-footer">
    <div class="footer-brand-panel">
      <div class="brand"><span class="brand-dot"></span>QM Volt</div>
    </div>
    <nav class="footer-nav">
      <a href="#">HOME</a>
      <a href="#">ABOUT US</a>
      <a href="#">BLOG</a>
    </nav>
    <p class="copyright">2011. QM Volt. All rights reserved.</p>
  </footer>
</body>
</html>
```